Trucking company specializing in intermodal containers

We need a logo design for our trucking company based in Kent, Washington. Our companies name is Dorvale Haulworks LLC, we specialize in intermodal containers, and work off of the Crestmark rail lines and the ports. We provide service by transporting freight with our fleet of trucks. We operate within Washington, Oregon, and Idaho. Our fleet consists of an east division and a local division. Our team motto currently is globally connected, locally invested.

Target Market(s)

brokers, intermodal management companies, customers

Industry/Entity Type

Trucking Company

Contact Information for Business Card

physical address 4519 N. 163rd Pl Kent, WA 98517
office number is 253-614-9026

Font styles to use
Sans Serif

Colors

Designer to choose colors to be used in the design.

Requirements
Must have
• We need to update our current logo. Something like an emblem; that makes a statement that this logo/ sign represents Dorvale Haulworks. Something like a royal stamp but in this case a royal shield.
Nice to have
• simple, yet bold. something someone does not currently have. We need something fresh and exciting. Something that will also make a statement because currently our reputation is great within the industry and our community. But we need to reflect that we are professional and willing to provide the best service. We are open to new statement lines.
Should not have
• Should not have something thats been used before. We are open to suggestions that you have and a design that is completely unique and you make originally without what we want but what you like as well. Ofcourse it should still represent the industry we are in.

```html
<!DOCTYPE html>
<html lang="en">
<head>
<meta charset="utf-8">
<title>Dorvale Haulworks LLC — Business Card</title>
<link href="https://fonts.googleapis.com/css2?family=Questrial&display=swap" rel="stylesheet">
<style>
  :root {
    --card-dark: #151515;
    --card-mid: #2f2f2f;
    --truck-tone: rgba(95, 95, 95, 0.38);
    --ink: #ffffff;
    --ink-soft: #f2f2f2;
  }
  html, body {
    margin: 0;
    padding: 0;
    width: 1200px;
    height: 702px;
    overflow: hidden;
    background: var(--card-dark);
  }
  .card {
    position: relative;
    width: 1200px;
    height: 702px;
    overflow: hidden;
    font-family: "Questrial", "Century Gothic", sans-serif;
    color: var(--ink);
    background: radial-gradient(ellipse at 55% 35%, var(--card-mid) 0%, var(--card-dark) 78%);
  }
  .truck-backdrop {
    position: absolute;
    left: 50px;
    top: 0;
    width: 1120px;
    height: 702px;
    background: radial-gradient(ellipse 52% 60% at 50% 52%, var(--truck-tone) 0%, rgba(60,60,60,0.18) 55%, rgba(20,20,20,0) 85%);
  }
  .brand {
    position: absolute;
    left: 0;
    top: 128px;
    width: 1200px;
    display: flex;
    justify-content: center;
    align-items: center;
    gap: 30px;
  }
  .brand-mark {
    width: 70px;
    height: 70px;
    background: var(--ink);
    flex: none;
  }
  .brand-name {
    font-size: 66px;
    line-height: 80px;
    letter-spacing: 3px;
    text-transform: uppercase;
    color: var(--ink);
    text-align: left;
  }
  .brand-city {
    position: absolute;
    left: 0;
    top: 350px;
    width: 1200px;
    text-align: center;
    font-size: 42px;
    line-height: 52px;
    color: var(--ink);
  }
  .contact {
    position: absolute;
    left: 0;
    top: 436px;
    width: 1200px;
    text-align: center;
    color: var(--ink-soft);
  }
  .contact-name { font-size: 34px; line-height: 40px; }
  .contact-title { font-size: 25px; line-height: 32px; margin-bottom: 20px; }
  .contact-phones { font-size: 27px; line-height: 36px; }
  .contact-email { font-size: 29px; line-height: 38px; }
  .contact-address { font-size: 27px; line-height: 38px; }
</style>
</head>
<body>
  <div class="card">
    <div class="truck-backdrop" role="img" aria-label="Faint line illustration of a semi truck cab behind the card content"></div>

    <div class="brand">
      <span class="brand-mark"></span>
      <div class="brand-name">Dorvale<br>Haulworks LLC</div>
    </div>
    <div class="brand-city">Kent, WA</div>

    <div class="contact">
      <div class="contact-name">Reid Calloway</div>
      <div class="contact-title">Operations Coordinator</div>
      <div class="contact-phones">Office: (253) 614-9026 | Fax: (253) 508-3372</div>
      <div class="contact-email">dispatch@dorvalehaulworks.com</div>
      <div class="contact-address">4519 N. 163rd Pl Kent, WA 98517</div>
    </div>
  </div>
</body>
</html>
```